Brumvale Business Card

I need something that flows with the logo and looks professional but creative. I included the thumbnail file of the photo but will upload the source file once I have it. Colors of business card should flow. I am interested in doing the translucent clear plastic cards as well. My company is called Brumvale in one word and the contact details are below:

Dean Holloway
832-574-2938
www.BrumvaleTx.example
dholloway_47@mailbox.example
Updates

Too much red. I'd rather focus on the blue and put some silver or grey in there.

New Files uploaded. Like the designs so far and am looking forward to seeing more.

Looking for a whole new direction. Let's forget about the plastic card. Let's focus on the blue more than red. I still haven't seen something that really grabs me.

Industry/Entity Type

Plastic

```html
<!DOCTYPE html>
<html lang="en">
<head>
<meta charset="utf-8">
<title>Brumvale Business Card</title>
<link href="https://fonts.googleapis.com/css2?family=Cinzel:wght@400;600;700&display=swap" rel="stylesheet">
<style>
  :root {
    --page-bg: #e6e4e1;
    --frost-top: #f4f3f1;
    --frost-mid: #e3e4e6;
    --frost-low: #d9dbde;
    --band-dark: #2b2727;
    --band-deep: #1e1b1b;
    --swoosh-red: #b3262f;
    --swoosh-blue: #1f5a8a;
    --silver: #d8d6d2;
    --brand-blue: #1d4f7a;
    --text-warm: #cdb79c;
    --icon-light: #e9e4dc;
  }
  * { margin: 0; padding: 0; box-sizing: border-box; }
  html, body {
    width: 1200px;
    height: 970px;
    overflow: hidden;
    background: var(--page-bg);
  }
  .card {
    position: absolute;
    left: 100px;
    top: 207px;
    width: 1000px;
    height: 556px;
    overflow: hidden;
    box-shadow: 0 10px 30px rgba(0,0,0,0.18);
    font-family: "Cinzel", serif;
  }
  .card-art {
    position: absolute;
    inset: 0;
    width: 100%;
    height: 100%;
  }
  .brand-name {
    position: absolute;
    left: 0;
    right: 0;
    top: 140px;
    text-align: center;
    font-family: "Cinzel", serif;
    font-weight: 600;
    font-size: 80px;
    letter-spacing: 2px;
    color: var(--brand-blue);
    line-height: 1;
  }
  .holder-name {
    position: absolute;
    left: 28px;
    top: 456px;
    font-weight: 700;
    font-size: 31px;
    color: var(--text-warm);
    letter-spacing: 0.5px;
    line-height: 1;
  }
  .contact-list {
    position: absolute;
    right: 26px;
    top: 420px;
    list-style: none;
  }
  .contact-item {
    display: flex;
    justify-content: flex-end;
    align-items: center;
    gap: 22px;
    height: 28px;
    font-size: 21px;
    color: var(--text-warm);
    line-height: 1;
  }
  .contact-item svg {
    width: 24px;
    height: 20px;
    flex: none;
  }
</style>
</head>
<body>
  <div class="card">
    <svg class="card-art" viewBox="0 0 1000 556" preserveAspectRatio="none" aria-hidden="true">
      <defs>
        <linearGradient id="frost" x1="0" y1="0" x2="0" y2="1">
          <stop offset="0" stop-color="var(--frost-top)"/>
          <stop offset="0.6" stop-color="var(--frost-mid)"/>
          <stop offset="1" stop-color="var(--frost-low)"/>
        </linearGradient>
        <linearGradient id="band" x1="0" y1="0" x2="1" y2="0">
          <stop offset="0" stop-color="var(--band-dark)"/>
          <stop offset="1" stop-color="var(--band-deep)"/>
        </linearGradient>
      </defs>
      <rect class="frost-panel" width="1000" height="556" fill="url(#frost)"/>
      <path class="swoosh-red" d="M0,295 C260,330 520,372 760,380 C560,392 260,360 0,322 Z" fill="var(--swoosh-red)"/>
      <path class="swoosh-blue" d="M240,372 C520,400 800,380 1000,302 L1000,322 C800,398 520,412 240,372 Z" fill="var(--swoosh-blue)"/>
      <path class="silver-line" d="M0,326 C300,372 620,408 1000,326" fill="none" stroke="var(--silver)" stroke-width="3"/>
      <path class="dark-band" d="M0,332 C300,378 620,414 1000,332 L1000,556 L0,556 Z" fill="url(#band)"/>
    </svg>

    <div class="brand-name">Brumvale</div>

    <div class="holder-name">Dean Holloway</div>

    <ul class="contact-list">
      <li class="contact-item">832-574-2938
        <svg viewBox="0 0 24 20" aria-hidden="true"><path d="M3,7 C3,3 21,3 21,7 L17,8 L16,6 L8,6 L7,8 Z M6,10 L18,10 L20,17 L4,17 Z" fill="var(--icon-light)"/></svg>
      </li>
      <li class="contact-item">dholloway_47@mailbox.example
        <svg viewBox="0 0 24 20" aria-hidden="true"><rect x="2" y="3" width="20" height="14" fill="none" stroke="var(--icon-light)" stroke-width="2"/><path d="M2,3 L12,11 L22,3 M2,17 L9,9 M22,17 L15,9" fill="none" stroke="var(--icon-light)" stroke-width="1.6"/></svg>
      </li>
      <li class="contact-item">www.BrumvaleTx.example
        <svg viewBox="0 0 24 20" aria-hidden="true"><rect x="3" y="2" width="18" height="12" fill="none" stroke="var(--icon-light)" stroke-width="2"/><path d="M9,18 L15,18 M12,14 L12,18" stroke="var(--icon-light)" stroke-width="2"/></svg>
      </li>
    </ul>
  </div>
</body>
</html>
```